女性向け商品としてターゲットは20代ー60代のナチュラル素材を使いたいという方向けです。
お通じの改善から抗酸化、抗糖化、食事の前に飲料頂くと、マンナンの成分が脂分、糖分の吸収を妨げてくれる商品になります。
MIRELA TIDEの意味は綺麗にどんどんループのように良くなる商品というコンセプトからの名前です。
イメージは「これを飲んでる私はおしゃれ・可愛い」と思っていただけるようなスタイリッシュなパッケージデザインを考えております。
真っ白なバックに、ポリッシュの磨きをかける、ツヤを出す、なめらかにする、光沢を出すという意味から中身の色がマニュキアのような溢れ方をしながらポリッシュ筆で書いたようなイメージです。(色は商品中身の色)

どうぞ宜しくお願い致します。
W1650m D1170m H280m
赤系、黄・オレンジ系
• 高解像度JPG (.jpg)
• イラストレーター形式 (.ai)
• フォトショップ形式 (.psd)
パッケージの紙質サイズの変更を追記させて頂きます。

コートボール 厚さ0.33mm
サイズ 162×118×29mm

どうぞ宜しくお願い致します。
ロゴに関してですが筆記体では無いものでご提案ください。
美容関係商品ですが、そこにこだわらず文字デザイン頂ければ幸いです。

ポスターまで作成いただいたことでよりイメージを自分自身も持て、自分と同じようなイメージで自分の商品を大切にしてくれるような思いで当選させて頂きました。

皆様この度は弊社コンペにご参加頂きまして誠にありがとうございました。
本当にいろんな形でご提案頂き感謝しております。

又このような形で出させていただいた際はまたご提案頂けたら幸いです。

有難うございました。

```html
<!DOCTYPE html>
<html lang="ja">
<head>
<meta charset="utf-8">
<title>MIRELA TIDE — パッケージ展開図</title>
<link rel="stylesheet" href="https://fonts.googleapis.com/css2?family=Poiret+One&family=Noto+Sans+JP:wght@400;500&display=swap">
<style>
  :root{
    --red:#e5162c;
    --red-deep:#b30f20;
    --red-mid:#d51a2e;
    --white:#ffffff;
    --grey-line:#b9b9b9;
    --grey-text:#9a9a9a;
    --canvas:#ffffff;
  }
  *{margin:0;padding:0;box-sizing:border-box}
  html,body{width:728px;height:1200px;overflow:hidden;background:var(--canvas)}
  .canvas{position:relative;width:728px;height:1200px}
  .panel{position:absolute;display:flex;align-items:center;justify-content:center;overflow:hidden}
  .brand{font-family:"Poiret One",sans-serif;letter-spacing:.14em;white-space:nowrap;font-weight:400}
  .flap-text{font-size:27px}
  .upside{transform:rotate(180deg)}
  .side-text{transform:rotate(90deg);font-size:24px}

  /* outer lid */
  .lid .face{left:100px;top:110px;width:536px;height:376px;
    background:radial-gradient(ellipse at 50% 48%,var(--red-mid) 0%,var(--red) 18%,var(--red-deep) 100%);
    flex-direction:column;color:var(--white)}
  .lid .flap-top{left:100px;top:24px;width:536px;height:86px;background:var(--red);color:var(--white)}
  .lid .flap-bottom{left:100px;top:486px;width:536px;height:84px;background:var(--red);color:var(--white)}
  .lid .flap-side{top:110px;width:76px;height:376px;background:var(--white);border:1.5px solid var(--grey-line);color:var(--grey-text)}
  .lid .left{left:24px;border-right:none}
  .lid .right{left:636px;border-left:none}

  /* inner tray */
  .tray .face{left:100px;top:730px;width:536px;height:314px;background:var(--white);
    border-top:1.5px solid var(--grey-line);border-bottom:1.5px solid var(--grey-line);
    flex-direction:column;color:var(--red)}
  .tray .flap-top{left:100px;top:644px;width:536px;height:86px;background:var(--white);
    border:1.5px solid var(--grey-line);border-bottom:none;color:var(--red)}
  .tray .flap-bottom{left:100px;top:1044px;width:536px;height:84px;background:var(--white);
    border:1.5px solid var(--grey-line);border-top:none;color:var(--red)}
  .tray .flap-side{top:730px;width:76px;height:314px;background:var(--red);color:var(--white)}
  .tray .left{left:24px}
  .tray .right{left:636px}

  .category{font-family:"Noto Sans JP",sans-serif;writing-mode:vertical-rl;font-size:12px;letter-spacing:.12em;margin-bottom:22px}
  .title{font-size:44px;letter-spacing:.16em}
  .count{margin-top:26px;font-family:"Noto Sans JP",sans-serif;font-weight:500;font-size:13px;
    padding:2px 10px;border-radius:12px;line-height:1.3}
  .lid .count{background:var(--white);color:var(--red-deep)}
  .tray .count{background:var(--red);color:var(--white)}
</style>
</head>
<body>
<div class="canvas">

  <section class="net lid" aria-label="外箱（ふた）展開図">
    <div class="panel flap-top"><span class="brand flap-text upside">MIRELA TIDE</span></div>
    <div class="panel flap-side left"><span class="brand side-text">MIRELA TIDE</span></div>
    <div class="panel face">
      <span class="category">粉末乳酸菌飲料</span>
      <span class="brand title">MIRELA TIDE</span>
      <span class="count">30包入</span>
    </div>
    <div class="panel flap-side right"><span class="brand side-text">MIRELA TIDE</span></div>
    <div class="panel flap-bottom"><span class="brand flap-text">MIRELA TIDE</span></div>
  </section>

  <section class="net tray" aria-label="内箱 展開図">
    <div class="panel flap-top"><span class="brand flap-text upside">MIRELA TIDE</span></div>
    <div class="panel flap-side left"><span class="brand side-text">MIRELA TIDE</span></div>
    <div class="panel face">
      <span class="category">粉末乳酸菌飲料</span>
      <span class="brand title">MIRELA TIDE</span>
      <span class="count">30包入</span>
    </div>
    <div class="panel flap-side right"><span class="brand side-text">MIRELA TIDE</span></div>
    <div class="panel flap-bottom"><span class="brand flap-text">MIRELA TIDE</span></div>
  </section>

</div>
</body>
</html>
```